Marwick Ostrand Law website for a law firm

modern clean website for a small boutique law firm. Based in Sacramento, CA and the Bay Area. Practice areas of Family Law, Civil litigation, and Criminal Defense. We already have a logo design as well as attorney pictures to include on page.
Would like images of California included on site.
Would like site to go with Logo that is already designed...blue/grey/white colors.

Industry/Entity Type

Law Firm

Number of Pages Required

5+ page

Requirements
Must have
• I already have several pages of content drafted. Just need the pages with images to input content. Must be clean and modern feel. Want it to reflect California and small boutique feel that is provided personalized legal attention.
• Must have a page where I can blog or post articles on.

```html
<!DOCTYPE html>
<html lang="en">
<head>
<meta charset="utf-8">
<title>Marwick Ostrand Law</title>
<link href="https://fonts.googleapis.com/css2?family=Open+Sans:wght@400;600;700&family=Raleway:wght@500;600;700&family=Lora:wght@400&display=swap" rel="stylesheet">
<style>
:root{
  --blue:#3f8bd0;
  --blue-dark:#2f74b5;
  --charcoal:#4a4a4a;
  --charcoal-deep:#3e3e3e;
  --ink:#2b2b2b;
  --muted:#6d6d6d;
  --light:#f1f1f1;
  --line:#d6d6d6;
  --teal:#1e9e8f;
  --sky:#25b1ec;
  --white:#ffffff;
}
*{box-sizing:border-box;margin:0;padding:0}
html,body{width:1200px;height:4100px;overflow:hidden}
body{position:relative;background:var(--white);font-family:"Open Sans",Arial,sans-serif;color:var(--ink)}
.abs{position:absolute}
.heading{font-family:"Raleway",Arial,sans-serif;font-weight:700}

/* header */
.brand{left:66px;top:34px;font-family:"Raleway",sans-serif;font-weight:600;font-size:36px;color:var(--blue);letter-spacing:1px;white-space:nowrap}
.social{top:34px;width:44px;height:44px;border-radius:50%;background:var(--charcoal)}
.call{left:958px;top:34px;display:flex;gap:10px;align-items:center}
.call small{display:block;font-size:11px;color:var(--muted);letter-spacing:1px}
.call strong{display:block;font-size:22px;color:var(--blue);font-weight:700}
.nav{left:0;top:110px;width:1200px;height:46px;background:var(--blue);display:flex;padding-left:94px;align-items:center}
.nav a{color:var(--white);font-size:14px;text-decoration:none;margin-right:94px;letter-spacing:.5px}

/* hero */
.hero{left:0;top:156px;width:1200px;height:610px;background:linear-gradient(180deg,#9fc3e6 0%,#cfd9e0 45%,#5b6b52 80%,#3d4a3a 100%)}
.hero-cut{left:0;top:560px}
.hero-card{left:720px;top:298px;width:480px;background:rgba(20,20,20,.72);padding:20px 24px 22px}
.hero-card h1{font-family:"Raleway",sans-serif;font-weight:500;font-size:26px;line-height:34px;color:var(--white)}
.btn{display:inline-block;background:var(--blue);color:var(--white);font-size:13px;padding:9px 18px;letter-spacing:.5px}

/* about */
.about-title{left:102px;top:856px;font-size:27px;color:var(--ink);white-space:nowrap}
.about-title span{font-weight:500;font-size:21px}
.about-rule{left:102px;top:902px;width:64px;height:4px;background:var(--teal)}
.about-photo{left:68px;top:924px;width:254px;height:170px;background:linear-gradient(135deg,#7a5a48,#3a3a3a 60%,#8c8c8c)}
.about-side{left:336px;top:930px;width:390px;font-size:14px;line-height:22px;color:var(--muted)}
.about-side h3{font-size:15px;color:var(--ink);font-weight:700;margin-bottom:4px}
.about-body{left:68px;top:1108px;width:660px;font-size:14px;line-height:24px;color:var(--muted)}
.read-more{font-size:13px;color:var(--blue-dark);margin-top:18px;display:block}
.question{left:779px;top:773px;width:325px;height:380px;background:var(--blue);padding:32px 24px}
.question h2{font-family:"Raleway",sans-serif;font-weight:700;font-size:26px;color:var(--white);margin-bottom:24px;white-space:nowrap}
.field{height:44px;background:var(--white);margin-bottom:26px;font-size:13px;color:#888;padding:13px 12px}
.submit{height:48px;background:#1f1f1f;color:var(--white);font-size:15px;text-align:center;line-height:48px;letter-spacing:.5px}

/* practice */
.practice-bg{left:0;top:1256px}
.section-title{width:1200px;left:0;text-align:center;font-size:30px}
.title-rule{left:270px;width:660px;height:1px;background:var(--line)}
.title-mark{left:588px;width:24px;height:24px}
.area{top:1488px;width:260px;text-align:center;color:var(--white)}
.area .icon{width:100px;height:100px;border-radius:50%;background:var(--blue);margin:0 auto 14px;display:flex;align-items:center;justify-content:center}
.area h3{font-family:"Raleway",sans-serif;font-weight:700;font-size:22px;margin-bottom:14px}
.area p{font-size:13px;line-height:22px;padding:0 16px;color:#e6e6e6}
.area .more{display:inline-block;margin-top:18px;font-size:12px;padding:4px 10px}
.area .more.boxed{border:1px solid var(--white)}
.chev{top:1580px}

/* understanding */
.laptop{left:137px;top:2099px;width:464px;height:288px}
.steps{left:680px;top:2104px;width:420px}
.step{margin-bottom:32px}
.step h4{font-size:15px;font-weight:700;color:var(--ink)}
.step p{font-size:13px;color:var(--muted);margin-top:4px}

/* testimonials */
.testi-bg{left:0;top:2470px}
.quote-badge{left:550px;top:2680px;width:100px;height:32px;background:var(--sky);color:var(--white);font-size:30px;text-align:center;line-height:40px;font-family:"Lora",serif}
.testi-head{left:0;top:2740px;width:1200px;text-align:center;font-family:"Lora",serif;font-size:22px;color:var(--blue)}
.testi-body{left:200px;top:2780px;width:800px;text-align:center;font-size:13px;line-height:20px;color:#8a8a8a}
.avatar{left:565px;top:2852px;width:70px;height:70px;border-radius:50%;background:linear-gradient(135deg,#c9a48a,#8a6a56)}
.testi-name{left:0;top:2950px;width:1200px;text-align:center;font-size:15px;font-weight:700;color:var(--ink)}
.testi-role{left:0;top:2972px;width:1200px;text-align:center;font-size:10px;font-weight:700;color:var(--sky);letter-spacing:.5px}
.round-arrow{top:2780px;width:46px;height:46px;border-radius:50%;background:var(--white);border:1px solid var(--line)}

/* map */
.map{left:0;top:3034px;width:1200px;height:416px;background:linear-gradient(135deg,#e4e4e4,#d3d3d3 50%,#e9e9e9)}

/* contact */
.contact{left:0;top:3449px;width:1200px;height:601px;background:var(--charcoal)}
.contact-form{left:118px;top:3635px;width:445px;height:342px;background:var(--light);padding:22px}
.contact-form h3{font-family:"Raleway",sans-serif;font-weight:600;font-size:24px;color:var(--ink);margin-bottom:14px}
.cf-field{height:40px;background:var(--white);margin-bottom:12px;font-size:13px;color:#999;padding:11px 10px}
.cf-field.tall{height:88px}
.cf-send{position:absolute;right:22px;bottom:20px;background:var(--blue);color:var(--white);font-size:12px;padding:9px 16px}
.company{left:599px;top:3638px;font-family:"Raleway",sans-serif;font-weight:700;font-size:28px;color:var(--white);white-space:nowrap}
.office{color:var(--white)}
.office h4{font-size:17px;font-weight:700;margin-bottom:12px}
.addr{display:flex;gap:12px;font-size:13px;line-height:18px;margin-bottom:10px}
.pin{width:22px;height:22px;border-radius:50%;background:var(--blue);flex:none;display:flex;align-items:center;justify-content:center}
.book{left:897px;top:3899px;width:156px;height:54px;background:var(--blue);border-radius:4px;color:var(--white);font-size:14px;display:flex;align-items:center;justify-content:center;gap:10px}
.footer{left:0;top:4050px;width:1200px;height:50px;background:var(--blue);color:var(--white);text-align:center;line-height:50px;font-size:13px}
</style>
</head>
<body>

<!-- header -->
<div class="abs brand">MARWICK OSTRAND LAW</div>
<div class="abs social" style="left:762px"></div>
<div class="abs social" style="left:824px"></div>
<div class="abs social" style="left:886px"></div>
<div class="abs call">
  <svg width="22" height="22" viewBox="0 0 24 24"><path fill="#4a4a4a" d="M6.6 10.8a15 15 0 0 0 6.6 6.6l2.2-2.2a1 1 0 0 1 1-.25 11.4 11.4 0 0 0 3.6.57 1 1 0 0 1 1 1V20a1 1 0 0 1-1 1A17 17 0 0 1 3 4a1 1 0 0 1 1-1h3.5a1 1 0 0 1 1 1 11.4 11.4 0 0 0 .57 3.6 1 1 0 0 1-.25 1z"/></svg>
  <div><small>CALL US NOW</small><strong>001 555 0142</strong></div>
</div>
<nav class="abs nav"><a>HOME</a><a>ABOUT US</a><a>PRACTICE AREAS</a><a>CONTACT US</a></nav>

<!-- hero -->
<div class="abs hero" role="img" aria-label="Photograph of the California State Capitol dome framed by palm trees"></div>
<svg class="abs hero-cut" width="1200" height="206" viewBox="0 0 1200 206">
  <polygon points="0,60 470,190 1200,60 1200,206 0,206" fill="#d9d9d9"/>
  <polygon points="0,90 470,206 1200,90 1200,206 0,206" fill="#ffffff"/>
</svg>
<div class="abs hero-card">
  <h1>AT MARWICK OSTRAND LAW, YOU ARE OUR FIRST PRIORITY</h1>
  <span class="btn" style="margin-top:14px">READ MORE</span>
</div>

<!-- about -->
<h2 class="abs heading about-title">ABOUT MARWICK OSTRAND <span>LAW GROUP PLLC</span></h2>
<div class="abs about-rule"></div>
<div class="abs about-photo" role="img" aria-label="Portrait photograph of an attorney seated in an office"></div>
<div class="abs about-side">
  <h3>WHAT ARE OUR ADVANTAGES?</h3>
  What does your company offer that will improve or solve a problem? Explain the pain point being alleviated right.
</div>
<div class="abs about-body">
  What does your company offer that will improve or solve a problem? Explain the pain point being alleviated right What does your company offer that will improve or solve a problem? Explain the pain point being alleviated right.
  <span class="read-more">Read More →</span>
</div>
<form class="abs question">
  <h2>HAVE A QUESTION?</h2>
  <div class="field">Your Name</div>
  <div class="field">Your Email</div>
  <div class="field">Phone No.</div>
  <div class="submit">GET STARTED</div>
</form>

<!-- practice areas -->
<svg class="abs practice-bg" width="1200" height="660" viewBox="0 0 1200 660">
  <polygon points="0,96 1200,0 1200,564 0,660" fill="#4a4a4a"/>
  <polygon points="0,600 1200,520 1200,564 0,660" fill="#3e3e3e"/>
</svg>
<h2 class="abs heading section-title" style="top:1348px;color:#fff">Practice Areas</h2>
<div class="abs title-rule" style="top:1412px;background:#777"></div>
<svg class="abs title-mark" style="top:1400px" viewBox="0 0 24 24"><rect x="2" y="2" width="20" height="20" fill="#4a4a4a"/><path d="M12 3l3 3-3 3-3-3zM12 15l3 3-3 3-3-3zM3 12l3-3 3 3-3 3zM15 12l3-3 3 3-3 3z" fill="#fff"/></svg>
<svg class="abs chev" style="left:14px" width="16" height="30" viewBox="0 0 16 30"><path d="M14 2L2 15l12 13" stroke="#fff" stroke-width="2" fill="none"/></svg>
<svg class="abs chev" style="left:1170px" width="16" height="30" viewBox="0 0 16 30"><path d="M2 2l12 13L2 28" stroke="#fff" stroke-width="2" fill="none"/></svg>

<div class="abs area" style="left:56px">
  <div class="icon"><svg width="44" height="44" viewBox="0 0 24 24"><path d="M12 3l7 3v5c0 5-3 8-7 10-4-2-7-5-7-10V6z" stroke="#fff" stroke-width="1.5" fill="none"/></svg></div>
  <h3>Criminal Defense</h3>
  <p>Estate planning is a process that involves examining your assets and liabilities, your personal and extended estate.</p>
  <span class="more">Read more →</span>
</div>
<div class="abs area" style="left:337px">
  <div class="icon"><svg width="44" height="44" viewBox="0 0 24 24"><path d="M6 3h9l4 4v14H6zM9 10h7M9 13h7M9 16h5" stroke="#fff" stroke-width="1.5" fill="none"/></svg></div>
  <h3>Estate Planning</h3>
  <p>Estate planning is a process that involves examining your assets and liabilities, your personal and extended estate.</p>
  <span class="more">Read more →</span>
</div>
<div class="abs area" style="left:613px">
  <div class="icon"><svg width="44" height="44" viewBox="0 0 24 24"><circle cx="12" cy="12" r="8" stroke="#fff" stroke-width="1.5" fill="none"/><path d="M7 10h10M7 14h10" stroke="#fff" stroke-width="1.5"/></svg></div>
  <h3>Civil Litigation</h3>
  <p>Estate planning is a process that involves examining your assets and liabilities, your personal and extended estate.</p>
  <span class="more boxed">Read more →</span>
</div>
<div class="abs area" style="left:889px">
  <div class="icon"><svg width="44" height="44" viewBox="0 0 24 24"><path d="M3 12l9-8 9 8M6 10v10h12V10M10 20v-5h4v5" stroke="#fff" stroke-width="1.5" fill="none"/></svg></div>
  <h3>Family Law</h3>
  <p>Estate planning is a process that involves examining your assets and liabilities, your personal and extended estate.</p>
  <span class="more">Read more →</span>
</div>

<!-- understanding -->
<h2 class="abs heading section-title" style="top:1940px;color:var(--ink)">Understanding You</h2>
<div class="abs title-rule" style="top:2004px"></div>
<svg class="abs title-mark" style="top:1992px" viewBox="0 0 24 24"><rect x="2" y="2" width="20" height="20" fill="#fff"/><path d="M12 3l3 3-3 3-3-3zM12 15l3 3-3 3-3-3zM3 12l3-3 3 3-3 3zM15 12l3-3 3 3-3 3z" fill="#2b2b2b"/></svg>
<svg class="abs laptop" viewBox="0 0 464 288">
  <rect x="40" y="0" width="384" height="256" rx="10" fill="#1e1e1e"/>
  <path d="M0 258h464l-20 22a10 10 0 0 1-8 4H28a10 10 0 0 1-8-4z" fill="#c9c9c9"/>
</svg>
<div class="abs" style="left:193px;top:2113px;width:352px;height:222px;background:linear-gradient(135deg,#8a4a36,#6c4a3c 45%,#2f2f2f)" role="img" aria-label="Photograph of two attorneys standing in an office"></div>
<div class="abs steps">
  <div class="step"><h4>IDENTIFY THE ISSUES</h4><p>We help you break down your legal problems</p></div>
  <div class="step"><h4>STRUCTURED ADVICE</h4><p>We give you clear legal advice about your options</p></div>
  <div class="step"><h4>RESEARCH &amp; ANALYSIS</h4><p>We examine your case to find the best solution for you</p></div>
  <div class="step"><h4>COMMUNICATING WITH YOU</h4><p>We provide you with regular updates about your matter</p></div>
</div>

<!-- testimonials -->
<svg class="abs testi-bg" width="1200" height="566" viewBox="0 0 1200 566">
  <polygon points="0,80 460,0 1200,110 1200,566 0,566" fill="#f2f2f2"/>
</svg>
<h2 class="abs heading section-title" style="top:2565px;color:var(--ink)">Our Testimonials</h2>
<div class="abs title-rule" style="top:2629px"></div>
<svg class="abs title-mark" style="top:2617px" viewBox="0 0 24 24"><rect x="2" y="2" width="20" height="20" fill="#f2f2f2"/><path d="M12 3l3 3-3 3-3-3zM12 15l3 3-3 3-3-3zM3 12l3-3 3 3-3 3zM15 12l3-3 3 3-3 3z" fill="#2b2b2b"/></svg>
<div class="abs quote-badge">“</div>
<div class="abs testi-head">At Trust, Each Lawyer Focuses Only On Civil Matters !</div>
<p class="abs testi-body">Our attorneys listened closely, explained every option in plain words and kept us informed at each step. We felt supported from the first call to the final hearing and would gladly return.</p>
<div class="abs round-arrow" style="left:76px"><svg width="44" height="44" viewBox="0 0 44 44"><path d="M25 15l-7 7 7 7" stroke="#999" stroke-width="2" fill="none"/></svg></div>
<div class="abs round-arrow" style="left:1066px"><svg width="44" height="44" viewBox="0 0 44 44"><path d="M19 15l7 7-7 7" stroke="#999" stroke-width="2" fill="none"/></svg></div>
<div class="abs avatar" role="img" aria-label="Client portrait photograph"></div>
<div class="abs testi-name">Elena Varga</div>
<div class="abs testi-role">CORPORATE LAWYER</div>

<!-- map -->
<div class="abs map" role="img" aria-label="Street map showing the office location"></div>
<svg class="abs" style="left:482px;top:3160px" width="48" height="64" viewBox="0 0 48 64">
  <path d="M24 2C12 2 3 11 3 23c0 16 21 39 21 39s21-23 21-39C45 11 36 2 24 2z" fill="#3f8bd0"/>
  <circle cx="24" cy="23" r="11" fill="#fff"/><path d="M24 17v12M18 23h12" stroke="#3f8bd0" stroke-width="2.5"/>
</svg>

<!-- contact -->
<div class="abs contact"></div>
<h2 class="abs heading section-title" style="top:3508px;color:#fff">Contact Us</h2>
<div class="abs title-rule" style="top:3572px;background:#777"></div>
<svg class="abs title-mark" style="top:3560px" viewBox="0 0 24 24"><rect x="2" y="2" width="20" height="20" fill="#4a4a4a"/><path d="M12 3l3 3-3 3-3-3zM12 15l3 3-3 3-3-3zM3 12l3-3 3 3-3 3zM15 12l3-3 3 3-3 3z" fill="#fff"/></svg>
<form class="abs contact-form">
  <h3>Contact form</h3>
  <div class="cf-field">Name</div>
  <div class="cf-field">Email</div>
  <div class="cf-field tall">Message</div>
  <span class="cf-send">SUBMIT</span>
</form>
<div class="abs company">A Boutique California Law Firm.</div>
<div class="abs office" style="left:604px;top:3698px;width:260px">
  <h4>Head Office</h4>
  <div class="addr"><span class="pin"><svg width="10" height="12" viewBox="0 0 10 12"><circle cx="5" cy="4.5" r="2.5" fill="#fff"/></svg></span><span>1420 Alder Row<br>Suite 205<br>Fair Oaks, CA 95628</span></div>
  <div class="addr"><span class="pin"><svg width="12" height="12" viewBox="0 0 24 24"><path fill="#fff" d="M6.6 10.8a15 15 0 0 0 6.6 6.6l2.2-2.2a1 1 0 0 1 1-.25 11.4 11.4 0 0 0 3.6.57 1 1 0 0 1 1 1V20a1 1 0 0 1-1 1A17 17 0 0 1 3 4a1 1 0 0 1 1-1h3.5a1 1 0 0 1 1 1 11.4 11.4 0 0 0 .57 3.6 1 1 0 0 1-.25 1z"/></svg></span><span>Phone: +1 (555) 014 2290</span></div>
</div>
<div class="abs office" style="left:882px;top:3698px;width:260px">
  <h4>West Coast Office</h4>
  <div class="addr"><span class="pin"><svg width="10" height="12" viewBox="0 0 10 12"><circle cx="5" cy="4.5" r="2.5" fill="#fff"/></svg></span><span>880 Harbor Loop<br>Suite 500<br>Larkfield, CA 94019</span></div>
</div>
<div class="abs office" style="left:604px;top:3868px;width:280px">
  <h4>Technical Center</h4>
  <div class="addr"><span class="pin"><svg width="10" height="12" viewBox="0 0 10 12"><circle cx="5" cy="4.5" r="2.5" fill="#fff"/></svg></span><span>4412 Cedar Bend Road<br>Suite 255<br>Willow Flats CA 95831</span></div>
</div>
<div class="abs book">
  <svg width="24" height="20" viewBox="0 0 24 20"><path d="M2 4h9a2 2 0 0 1 2 2v12a2 2 0 0 0-2-2H2zM22 4h-9M22 4v12h-9" stroke="#fff" stroke-width="1.5" fill="none"/></svg>
  BOOK NOW
</div>
<footer class="abs footer">© 2017: Marwick Ostrand Law | All Right Reserved</footer>

</body>
</html>
```